Hello my name is Colin, I am Starting a business called Harbor Health and fitness and am in need of a memorable business card.
It is a personal training studio. I have added the logo that i would like to be on the left center om my business card. i would like room left up the top for a heading sentence such as. "Is your body shocking for all the wrong reasons". there must be room left on the right of the logo below the main heading for 3 sub headings.
then under those 3 headings and logo room for another larger heading eg. "give me a call and learn how to eat chocolate, drink bear and have great sex". in what room is left i would like to be used for my contact details, use I'm Colin Fairweather your fitness expert on the left then on the right Phone, Email and website space in at least 12 Point. Very specific i know :) now onto the back, for the back i would like an eye catching graphic and room for one main headline and 3 bullet points centered just write anything i will choose what to put in them when i pick a winner. Thank you very much for sticking through all of that :) i appreciate you taking the time to read it and hopefully undergo designing me a business card.
I can't wait to see the designs!

Target Market(s)

slightly more towards females although it would probably be best if it was targeted towards both sexes

Industry/Entity Type

Training

Requirements
Nice to have
• I would love to see if anyone could come up with a design that would really make my card stand out and be memorable.
Should not have
• tacky fitness photos of abs and muscles etc.

```html
<!DOCTYPE html>
<html lang="en">
<head>
<meta charset="utf-8">
<title>Harbor Health and Fitness – Business Card</title>
<link href="https://fonts.googleapis.com/css2?family=Questrial&family=Yanone+Kaffeesatz:wght@400&family=Righteous&display=swap" rel="stylesheet">
<style>
  :root {
    --stage: #8a8a8a;
    --card-black: #070809;
    --card-blue: #0a1cf2;
    --brand-red: #b00d0d;
    --ink-white: #f4eef4;
    --ink-black: #070809;
  }
  * { margin: 0; padding: 0; box-sizing: border-box; }
  html, body { width: 1200px; height: 1163px; overflow: hidden; }
  body { background: var(--stage); position: relative; }

  .card {
    position: absolute;
    width: 930px;
    height: 460px;
    left: 135px;
    overflow: hidden;
    background: var(--card-black);
  }
  .card--front { top: 70px; }
  .card--back  { top: 640px; }
  .card__bands { position: absolute; inset: 0; }

  .brand {
    position: absolute;
    left: 30px; top: 30px;
    color: var(--brand-red);
    font-family: "Questrial", sans-serif;
    font-weight: 400;
    line-height: 1;
  }
  .brand__name { display: block; font-size: 84px; letter-spacing: -1px; }
  .brand__tag  { display: block; font-size: 24px; margin-top: 4px; margin-left: 72px; }

  .quote {
    position: absolute;
    color: var(--ink-white);
    font-family: "Yanone Kaffeesatz", sans-serif;
    text-align: center;
    line-height: 1.25;
    white-space: nowrap;
  }
  .quote--left  { left: 50px;  top: 165px; width: 260px; font-size: 27px; }
  .quote--right { left: 430px; top: 100px; width: 480px; font-size: 29px; }

  .contact-name {
    position: absolute;
    left: 220px; top: 280px;
    font-family: "Righteous", sans-serif;
    white-space: nowrap;
  }
  .contact-name__person { display: block; color: var(--brand-red); font-size: 38px; letter-spacing: 1px; }
  .contact-name__role   { display: block; color: var(--ink-white); font-size: 26px; margin-left: 50px; letter-spacing: 1px; }

  .brand--back { left: 45px; top: 150px; }
  .brand--back .brand__name { font-size: 76px; }

  .contact-label {
    position: absolute;
    color: var(--ink-white);
    font-family: "Righteous", sans-serif;
    font-size: 30px;
    letter-spacing: 1px;
  }
  .contact-label--phone { left: 45px;  top: 400px; }
  .contact-label--email { left: 420px; top: 370px; }
</style>
</head>
<body>

  <section class="card card--front" aria-label="Card front">
    <svg class="card__bands" width="930" height="460" viewBox="0 0 930 460" aria-hidden="true">
      <polygon points="230,0 700,0 230,460 0,460 0,230" fill="var(--card-blue)"/>
      <polygon points="930,240 930,460 710,460" fill="var(--card-blue)"/>
    </svg>
    <div class="brand">
      <span class="brand__name">Harbor</span>
      <span class="brand__tag">Health and Fitness</span>
    </div>
    <p class="quote quote--left">"Is your body shocking<br>for all the wrong reasons".</p>
    <p class="quote quote--right">"Give me a call and learn how to eat chocolate,<br>drink beer and have great sex"</p>
    <div class="contact-name">
      <span class="contact-name__person">Colin Fairweather</span>
      <span class="contact-name__role">your fitness expert</span>
    </div>
  </section>

  <section class="card card--back" aria-label="Card back">
    <svg class="card__bands" width="930" height="460" viewBox="0 0 930 460" aria-hidden="true">
      <polygon points="240,0 840,0 930,95 930,460 700,460" fill="var(--card-blue)"/>
      <polygon points="0,290 0,460 170,460" fill="var(--card-blue)"/>
      <g class="band-lettering" fill="var(--ink-black)" font-family="Questrial, sans-serif" font-size="50">
        <text transform="translate(400,50) rotate(45)">Health and Fitness</text>
        <text transform="translate(540,40) rotate(45)">Health and Fitness</text>
      </g>
    </svg>
    <div class="brand brand--back">
      <span class="brand__name">Harbor</span>
    </div>
    <span class="contact-label contact-label--phone">Phone:</span>
    <span class="contact-label contact-label--email">E-mail:</span>
  </section>

</body>
</html>
```